E-brochure to promote our franchise opportunity to potential finance professionals

We need my words putting into a brochure, setting out, adding photographs and images ready for publication as a .pdf
The brochure needs to be readable as a pdf, I have no plans to publish on paper so should be well structured for a screen or tablet - easy navigation and a positive and striking visual feel

Target Market(s)

Potential business owners in business finance arranging - existing business bankers leaving their post, mortgage brokers expanding their business or existing commercial finance brokers looking for a means to expand their reach and have the help and support of a franchisor organisation

Industry/Entity Type

Finance

Font styles to use
Serif
Script

Colors
0555a3
eaf2ce

Requirements
Must have
• The project must have a professional but still accessible feel, we are not aiming to be a "corporate" like a merchant bank, our clients are ordinary small business owners, like you, so we need to speak their language. Our business is about the people we help, the dreams that come true because we help them and the wealth we create for them.
Nice to have
• Great artwork, interesting photographs, a compelling front cover page, pages which are easily readable, not too text heavy but getting the point across
Should not have
• Should not be boring - over corporate or too frivolous

```html
<!DOCTYPE html>
<html lang="en">
<head>
<meta charset="utf-8">
<title>Oakleaf.capital – Franchise opportunity</title>
<link rel="stylesheet" href="https://fonts.googleapis.com/css2?family=Crimson+Pro:wght@400;700&family=Tinos&display=swap">
<style>
  :root {
    --navy: #1c2e55;
    --sage: #b4c2bb;
    --paper: #ffffff;
    --rule: #a9aec4;
    --edge: #e6eeee;
    --photo-paper: #e4f0ee;
    --photo-teal: #a9cac6;
    --photo-desk: #8a8272;
    --photo-deep: #4e6466;
    --ink: #111111;
  }
  * { margin: 0; padding: 0; box-sizing: border-box; }
  html, body { width: 900px; height: 1200px; overflow: hidden; background: var(--paper); }
  .cover {
    position: relative;
    width: 900px;
    height: 1200px;
    overflow: hidden;
    background: var(--paper);
    color: var(--navy);
    font-family: "Crimson Pro", serif;
  }
  .band-edge,
  .photo-band {
    position: absolute;
    inset: 0;
  }
  .band-edge { background: var(--edge); }
  .band-edge--top { clip-path: polygon(478px 0, 900px 0, 900px 22px, 514px 432px, 72px 432px); }
  .band-edge--bottom { clip-path: polygon(836px 630px, 900px 630px, 900px 1062px, 404px 1062px); }
  .photo-band--top {
    clip-path: polygon(500px 0, 890px 0, 502px 432px, 96px 432px);
    background:
      radial-gradient(ellipse 220px 120px at 470px 300px, rgba(255,255,255,.75), transparent 70%),
      radial-gradient(ellipse 160px 80px at 300px 410px, rgba(60,70,72,.55), transparent 70%),
      linear-gradient(160deg, var(--photo-paper) 0%, var(--photo-teal) 35%, var(--photo-desk) 62%, var(--photo-deep) 100%);
  }
  .photo-band--bottom {
    clip-path: polygon(858px 630px, 900px 630px, 900px 1062px, 428px 1062px);
    background:
      radial-gradient(ellipse 180px 110px at 690px 900px, rgba(255,255,255,.65), transparent 70%),
      radial-gradient(ellipse 200px 60px at 640px 1040px, rgba(60,70,72,.5), transparent 70%),
      linear-gradient(200deg, var(--photo-paper) 0%, var(--photo-teal) 40%, var(--photo-desk) 75%, var(--photo-deep) 100%);
  }
  .brand {
    position: absolute;
    left: 80px;
    top: 470px;
    display: flex;
    align-items: flex-start;
    gap: 16px;
  }
  .brand__dot {
    flex: none;
    width: 112px;
    height: 112px;
    border-radius: 50%;
    border: 5px solid var(--sage);
  }
  .brand__text { padding-top: 4px; }
  .brand__name {
    font-size: 72px;
    font-weight: 400;
    line-height: 1;
    color: var(--navy);
  }
  .brand__tagline {
    font-family: "Tinos", serif;
    font-size: 26px;
    color: var(--sage);
    margin-top: 10px;
  }
  .pillars {
    position: absolute;
    left: 197px;
    top: 702px;
    list-style: none;
  }
  .pillars__item {
    display: flex;
    align-items: center;
    gap: 24px;
    height: 73px;
    font-size: 26px;
  }
  .pillars__icon { width: 58px; height: 58px; flex: none; }
  .cover__title {
    position: absolute;
    left: 81px;
    top: 1000px;
    font-size: 32px;
    font-weight: 700;
  }
  .cover__rule {
    position: absolute;
    left: 0;
    top: 1062px;
    width: 900px;
    height: 1px;
    background: var(--rule);
  }
  .credits {
    position: absolute;
    left: 81px;
    top: 1083px;
    font-family: "Tinos", serif;
    font-size: 17px;
    line-height: 22px;
    color: var(--ink);
  }
  .website {
    position: absolute;
    right: 80px;
    top: 1105px;
    font-family: "Tinos", serif;
    font-size: 17px;
    color: var(--ink);
  }
</style>
</head>
<body>
<main class="cover">
  <div class="band-edge band-edge--top"></div>
  <div class="photo-band photo-band--top" role="img" aria-label="Photograph of hands writing on financial papers beside a laptop on a desk"></div>
  <div class="band-edge band-edge--bottom"></div>
  <div class="photo-band photo-band--bottom" role="img" aria-label="Photograph of hands reviewing documents with a pen next to a laptop"></div>

  <div class="brand">
    <span class="brand__dot"></span>
    <div class="brand__text">
      <div class="brand__name">Oakleaf.capital</div>
      <div class="brand__tagline">Every business, every investor - Funded</div>
    </div>
  </div>

  <ul class="pillars">
    <li class="pillars__item">
      <svg class="pillars__icon" viewBox="0 0 58 58" aria-hidden="true"><circle cx="29" cy="29" r="25" fill="none" stroke="#1c2e55" stroke-width="3"/><path d="M17 30l8 8 16-17" fill="none" stroke="#1c2e55" stroke-width="3.5" stroke-linecap="round" stroke-linejoin="round"/></svg>
      Every Business
    </li>
    <li class="pillars__item">
      <svg class="pillars__icon" viewBox="0 0 58 58" aria-hidden="true"><circle cx="29" cy="29" r="25" fill="none" stroke="#1c2e55" stroke-width="3"/><path d="M17 30l8 8 16-17" fill="none" stroke="#1c2e55" stroke-width="3.5" stroke-linecap="round" stroke-linejoin="round"/></svg>
      Every Investor
    </li>
    <li class="pillars__item">
      <svg class="pillars__icon" viewBox="0 0 58 58" aria-hidden="true"><circle cx="29" cy="29" r="25" fill="none" stroke="#1c2e55" stroke-width="3"/><path d="M17 30l8 8 16-17" fill="none" stroke="#1c2e55" stroke-width="3.5" stroke-linecap="round" stroke-linejoin="round"/></svg>
      Funded
    </li>
  </ul>

  <h1 class="cover__title">Franchise opportunity</h1>
  <div class="cover__rule"></div>

  <p class="credits">
    Prepared for:<br>
    Prepared by: Daniel Hart, Principal.<br>
    3 October 2016
  </p>
  <p class="website">www.oakleaf.capital</p>
</main>
</body>
</html>
```